Referral Club PostCard/ Index Card

I need to create an Index card for a Contractor Referral Club. I already did my own door hanger which I can show you. Cost is a factor because I'm just starting my company. You guys have already created my 2 logos when I did a previous logo project so I want to use those logos and colors to create a scheme double sided postcard for my referral club attached to our some examples of other ones I've seen. So, you can 1 of 3 different design/color schemes as a basis:
1) The Black background with Blue Shield
2). The Light Blue background with the white wave (Really like this and the black one)
3). My White background blue/black business card design.
So, 3 different design/color schemes to attack?

You can also look at my website for ideas

http://www.TheLanternPointGuide.example
Updates

I have a picture of the things I want to say on BOTH sides on the Index card/[Post card. Basically, there are two versions that can be created, one with the black background/blue logo motif or one with the white/blue background logo. I bought BOTH designs in my logo contest. Actually 1 is the front of the cards and the other is the back of my card. I'm looking for creativity to get these contractors to join this referral club so I can get more leads.

I have some new logos,, icons and pdfs to submit for consideration

Target Market(s)

Drawing Other Contractors into my Professional Referral Exchange Club

Industry/Entity Type

Public Insurance Adjusting

Font styles to use
Serif
Sans Serif
Other font styles liked:
• Love Zurich font but very few people have it..It is eye drawing!!

Colors
0054AA
0677BA
7BADD7
CADEEF
E8F1F8
0094D4
00A9DD
6FCCEA
C7EBF8
E9F6FB
EE7325
F08F49
F5BC92
FAE3D3
FDF4ED

Requirements
Must have
• My Blue or Black/White color scheme to stay consistent to what Ive already had done
Nice to have
• Something that jumps off to entice them to join that I haven't thought of.

```html
<!DOCTYPE html>
<html lang="en">
<head>
<meta charset="utf-8">
<title>The Lantern Point Guide – Referral Club Postcard</title>
<link rel="stylesheet" href="https://fonts.googleapis.com/css2?family=Open+Sans:ital,wght@0,400;0,600;0,700;0,800;1,800&family=Roboto+Condensed:wght@700&family=Tinos:wght@400;700&display=swap">
<style>
  :root {
    --stage: #d4d4d4;
    --ink: #111111;
    --night: #000000;
    --navy: #0054aa;
    --royal: #1a2fb8;
    --blue: #0677ba;
    --sky: #0094d4;
    --cyan: #00a9dd;
    --ice: #6fccea;
    --mist: #cadeef;
    --paper: #ffffff;
    --orange: #f08f49;
    --gold: #f5b23d;
    --red: #e8231f;
    --slate: #1d4f6e;
    --grey-text: #3a3a3a;
  }
  * { box-sizing: border-box; margin: 0; padding: 0; }
  html, body { width: 1200px; height: 638px; overflow: hidden; }
  body {
    background: var(--stage);
    font-family: "Open Sans", Arial, sans-serif;
    position: relative;
  }
  .postcard {
    position: absolute;
    top: 119px;
    width: 570px;
    height: 400px;
    overflow: hidden;
    box-shadow: 0 6px 18px rgba(0,0,0,.25);
  }

  /* ---------- Back side: reasons ---------- */
  .postcard--reasons { left: 20px; background: var(--night); color: var(--paper); }
  .reasons__title-band {
    position: absolute; left: 0; top: 0; width: 100%; height: 46px;
    background: linear-gradient(90deg, var(--sky), var(--cyan) 60%, var(--blue));
    border-bottom: 4px solid var(--navy);
    display: flex; align-items: center; justify-content: center;
  }
  .reasons__title {
    font-weight: 800; font-size: 25px; letter-spacing: 1.5px;
    color: var(--paper); text-transform: uppercase;
  }
  .brand-lockup {
    position: absolute; left: 18px; top: 86px; width: 190px;
    display: flex; flex-direction: column; align-items: center; gap: 10px;
  }
  .brand-lockup__dot {
    width: 54px; height: 54px; border-radius: 50%; background: var(--blue);
  }
  .brand-lockup__name {
    font-family: "Open Sans", Arial, sans-serif; font-weight: 600;
    font-size: 19px; line-height: 1.2; color: var(--cyan);
    text-align: center; text-transform: uppercase;
  }
  .rating { position: absolute; left: 18px; top: 240px; width: 190px; text-align: center; }
  .rating__grade {
    font-family: "Open Sans", Arial, sans-serif; font-weight: 700;
    font-size: 24px; color: var(--red); line-height: 1;
  }
  .rating__note {
    font-family: "Tinos", "Times New Roman", serif; font-size: 12px;
    line-height: 1.1; margin-top: 3px; color: var(--paper);
  }
  .rating__source { font-family: "Tinos", "Times New Roman", serif; font-size: 7px; color: #bbbbbb; }
  .reasons__list {
    position: absolute; left: 222px; top: 60px; width: 330px;
    list-style: none; display: flex; flex-direction: column; gap: 10px;
  }
  .reason { display: flex; gap: 8px; font-size: 11.5px; line-height: 1.4; }
  .reason__number {
    flex: 0 0 22px; height: 22px; border-radius: 50%;
    background: var(--navy); border: 2px solid var(--gold);
    color: var(--paper); font-weight: 700; font-size: 12px;
    display: flex; align-items: center; justify-content: center;
  }
  .reasons__service {
    position: absolute; left: 0; right: 0; top: 300px; text-align: center;
    color: var(--gold); font-weight: 700; font-size: 14px;
  }
  .reasons__contact {
    position: absolute; left: 14px; right: 14px; top: 321px;
    display: flex; flex-wrap: wrap; align-items: center; justify-content: center;
    column-gap: 6px; row-gap: 2px;
    font-weight: 700; font-size: 11px; line-height: 16px; color: var(--paper);
  }
  .reasons__contact-item { display: inline-flex; align-items: center; gap: 5px; white-space: nowrap; }
  .reasons__contact-item svg { flex: 0 0 12px; }
  .reasons__foot {
    position: absolute; left: 0; bottom: 0; width: 100%; height: 40px;
  }

  /* ---------- Front side: join ---------- */
  .postcard--join { left: 610px; background: var(--paper); }
  .join__swoosh { position: absolute; inset: 0; }
  .join__brand { position: absolute; left: 34px; top: 24px; display: flex; align-items: center; gap: 12px; }
  .join__brand-dot { width: 48px; height: 48px; border-radius: 50%; background: var(--blue); }
  .join__brand-name {
    font-family: "Tinos", "Times New Roman", serif; font-weight: 700;
    font-size: 22px; color: var(--royal); line-height: 1.1;
  }
  .join__club {
    position: absolute; left: 94px; top: 78px; width: 285px;
    font-family: "Open Sans", Arial, sans-serif; font-weight: 700;
    font-size: 11.5px; color: var(--royal); line-height: 1.35;
  }
  .join__tagline {
    display: block; margin-top: 2px;
    font-family: "Tinos", "Times New Roman", serif; font-weight: 400;
    font-size: 10.5px; line-height: 1.3; color: var(--sky); letter-spacing: 1.2px; text-transform: uppercase;
  }
  .join__art {
    position: absolute; right: 40px; top: 8px; width: 130px; height: 170px;
    background: linear-gradient(180deg, #c8c8c8, #7d7d7d 55%, #9fae8e);
    border-radius: 4px;
  }
  .join__badge {
    position: absolute; right: 18px; top: 132px; width: 92px; height: 92px;
    border-radius: 50%; background: var(--blue); border: 4px solid var(--paper);
    box-shadow: 0 0 0 2px var(--blue);
  }
  .join__cta {
    position: absolute; left: 18px; top: 168px; width: 150px;
    display: flex; flex-direction: column; align-items: center; gap: 6px;
    font-weight: 700; font-size: 11px; letter-spacing: 1px; color: var(--ink);
  }
  .join__cta-pill {
    background: linear-gradient(135deg, var(--navy), var(--sky));
    color: var(--paper); border-radius: 40px; padding: 10px 14px;
    font-size: 12px; letter-spacing: 1.5px; border: 2px solid var(--mist);
  }
  .join__why {
    position: absolute; left: 180px; top: 198px; width: 360px; text-align: center;
  }
  .join__why-heading { font-weight: 700; font-size: 14px; color: var(--royal); margin-bottom: 4px; }
  .join__why-body { font-size: 10.5px; line-height: 1.45; color: var(--grey-text); }
  .join__service-band {
    position: absolute; left: 30px; right: 18px; top: 290px; height: 42px;
    border-radius: 22px;
    background: linear-gradient(90deg, var(--sky), var(--navy) 70%, var(--royal));
    display: flex; align-items: center; justify-content: center;
    font-weight: 700; font-size: 19px; color: var(--paper); white-space: nowrap;
  }
  .join__call {
    position: absolute; left: 0; right: 0; top: 338px; text-align: center;
    font-family: "Roboto Condensed", "Arial Narrow", sans-serif; font-weight: 700;
    font-size: 44px; color: var(--slate); letter-spacing: .5px;
  }
</style>
</head>
<body>

<section class="postcard postcard--reasons" aria-label="Referral club postcard, reasons side">
  <header class="reasons__title-band">
    <h1 class="reasons__title">Top Reasons For Joining Club</h1>
  </header>

  <div class="brand-lockup">
    <span class="brand-lockup__dot"></span>
    <p class="brand-lockup__name">The Lantern Point Guide</p>
  </div>

  <div class="rating">
    <p class="rating__grade">A+ Rating</p>
    <p class="rating__note">Highest Rating For<br>Public Insurance Adjusters</p>
    <p class="rating__source">(Source: Industry Reviews)</p>
  </div>

  <ol class="reasons__list">
    <li class="reason"><span class="reason__number">1</span><span>Lorem Ipsum is simply dummy text of the printing and typesetting industry. Lorem Ipsum has been the industry's standard dummy text.</span></li>
    <li class="reason"><span class="reason__number">2</span><span>Lorem Ipsum is simply dummy text of the printing and typesetting industry. Lorem Ipsum has been the industry's standard dummy text.</span></li>
    <li class="reason"><span class="reason__number">3</span><span>Lorem Ipsum is simply dummy text of the printing and typesetting industry. Lorem Ipsum has been the industry's standard dummy text.</span></li>
    <li class="reason"><span class="reason__number">4</span><span>Lorem Ipsum is simply dummy text of the printing and typesetting industry. Lorem Ipsum has been the industry's standard dummy text.</span></li>
  </ol>

  <p class="reasons__service">Servicing but not limited to</p>
  <p class="reasons__contact">
    <span class="reasons__contact-item">Florida, Alabama, Mississippi, and Louisiana.</span>
    <span class="reasons__contact-item">
      <svg width="12" height="12" viewBox="0 0 24 24" aria-hidden="true"><path fill="#f5b23d" d="M6.6 10.8a15.1 15.1 0 0 0 6.6 6.6l2.2-2.2c.3-.3.7-.4 1-.2 1.1.4 2.3.6 3.6.6.6 0 1 .4 1 1V20c0 .6-.4 1-1 1A17 17 0 0 1 3 4c0-.6.4-1 1-1h3.5c.6 0 1 .4 1 1 0 1.3.2 2.5.6 3.6.1.3 0 .7-.2 1z"/></svg>
      850-555-0147
    </span>
    <span class="reasons__contact-item">
      <svg width="12" height="12" viewBox="0 0 24 24" aria-hidden="true"><rect x="2" y="5" width="20" height="14" rx="2" fill="#f5b23d"/><path d="M3 6l9 7 9-7" stroke="#000" stroke-width="1.6" fill="none"/></svg>
      jordan@TheLanternPointGuide.example
    </span>
  </p>

  <svg class="reasons__foot" viewBox="0 0 570 40" preserveAspectRatio="none" aria-hidden="true">
    <rect x="0" y="4" width="570" height="6" fill="#cadeef"/>
    <rect x="0" y="12" width="570" height="28" fill="#0054aa"/>
    <rect x="0" y="12" width="330" height="28" fill="#0094d4"/>
  </svg>
</section>

<section class="postcard postcard--join" aria-label="Referral club postcard, join side">
  <svg class="join__swoosh" viewBox="0 0 570 400" preserveAspectRatio="none" aria-hidden="true">
    <path d="M0 300 C 120 230, 300 170, 570 165 L570 180 C 320 185, 140 240, 0 320 Z" fill="#0094d4"/>
    <path d="M0 320 C 140 250, 320 195, 570 185 L570 196 C 330 205, 150 262, 0 336 Z" fill="#cadeef"/>
    <path d="M0 336 C 150 270, 340 215, 570 200 L570 206 C 340 222, 160 282, 0 346 Z" fill="#7badd7"/>
    <rect x="0" y="392" width="570" height="8" fill="#0054aa"/>
  </svg>

  <div class="join__brand">
    <span class="join__brand-dot"></span>
    <p class="join__brand-name">The Lantern Point Guide</p>
  </div>
  <p class="join__club">
    Referral Exchange Club<br>
    Expert Public Adviser &amp; Loss Consultants
    <span class="join__tagline">Insurance Claim Experts<br>“For the Policyholder!!”</span>
  </p>

  <div class="join__art" role="img" aria-label="Illustration of a house resting on a stack of banknotes"></div>
  <div class="join__badge" role="img" aria-label="Award badge"></div>

  <div class="join__cta">
    <span>TO JOIN CLUB CLICK</span>
    <span class="join__cta-pill">PROFILE:EXAMPLE</span>
    <span>ON THIS LINK</span>
  </div>

  <div class="join__why">
    <h2 class="join__why-heading">Why The Lantern Point?</h2>
    <p class="join__why-body">Lorem Ipsum is simply dummy text of the printing and typesetting industry. Lorem Ipsum has been the industry's standard dummy text ever since the 1500s, when an unknown printer took a galley of type and scrambled it to make a type specimen book.</p>
  </div>

  <p class="join__service-band">Serving Florida | Borgia | Alabama &amp; Mississippi</p>
  <p class="join__call">Call:- 800-555-0123</p>
</section>

</body>
</html>
```